Voltren Assemblies, Inc. Business Card

Voltren has three operating entities and I'm looking for a standard business card template that can be used for Voltren and the three operating entities that the logo just get swapped out, but has a very similar look and feel. Ultimately if someone had a business card from each, they assume the organizations are related because they all have the same look and feel.
Below are our websites and I will attached the logos for each entity:
https://www.voltrenassemblies-example.com/
https://www.brackwayceramic-example.com/
https://www.omdr-pqsx-example.com/
https://www.tamberlinebreaker-example.com/

Target Market(s)

US Voltren

Industry/Entity Type

US Voltren

Contact Information for Business Card

Normal stuff

```html
<!DOCTYPE html>
<html lang="en">
<head>
<meta charset="utf-8">
<title>Voltren Assemblies, Inc. – Business Card Family</title>
<link rel="stylesheet" href="https://fonts.googleapis.com/css2?family=Josefin+Sans:wght@400;600;700&display=swap">
<style>
  :root {
    --sheet: #ffffff;
    --card-edge: #1a1a1a;
    --photo-light: #f1f2f3;
    --photo-mid: #dcdde0;
    --photo-dark: #c9cacd;
    --band-top: #0c1128;
    --band-mid: #141d40;
    --band-low: #1f2d63;
    --ink-light: #ffffff;
    --brand-navy: #1f2d63;
    --brand-steel: #4a7189;
    --brand-deep: #0a1470;
  }
  * { box-sizing: border-box; margin: 0; padding: 0; }
  html, body { width: 1200px; height: 900px; overflow: hidden; background: var(--sheet); }
  body { position: relative; font-family: "Josefin Sans", sans-serif; }

  .card {
    position: absolute;
    width: 534px; height: 297px;
    border: 1.5px solid var(--card-edge);
    background: var(--sheet);
  }
  .card--voltren    { left: 50px;  top: 133px; }
  .card--brackway   { left: 616px; top: 133px; }
  .card--tamberline { left: 50px;  top: 470px; }
  .card--orrick     { left: 616px; top: 470px; }

  .card__backdrop {
    position: absolute; left: 9px; top: 9px; width: 514px; height: 277px;
    background:
      linear-gradient(180deg, rgba(255,255,255,.55) 0%, rgba(255,255,255,0) 35%, rgba(255,255,255,.2) 100%),
      linear-gradient(90deg, var(--photo-mid) 0%, var(--photo-light) 30%, var(--photo-dark) 60%, var(--photo-mid) 100%);
  }

  .brand {
    position: absolute; left: 9px; top: 9px; width: 330px; height: 277px;
    display: flex; flex-direction: column; align-items: center; justify-content: center;
    gap: 10px; text-align: center;
  }
  .brand__mark {
    width: 74px; height: 74px; border-radius: 50%;
  }
  .brand__name {
    font-weight: 700; font-size: 28px; letter-spacing: .5px; line-height: 1.05;
    text-transform: uppercase;
  }
  .brand__tagline { font-size: 11px; font-weight: 400; letter-spacing: .3px; }
  .card--voltren .brand__mark { background: var(--brand-navy); }
  .card--voltren .brand__name { color: var(--brand-navy); font-size: 34px; }
  .card--voltren .brand__tagline { color: var(--brand-navy); font-size: 13px; letter-spacing: 4px; text-transform: uppercase; }
  .card--brackway .brand__name { color: var(--brand-navy); }
  .card--brackway .brand__tagline { color: var(--brand-navy); }
  .card--brackway .brand__mark { background: var(--brand-navy); border-radius: 0; }
  .card--tamberline .brand__name { color: var(--brand-steel); }
  .card--tamberline .brand__tagline { color: var(--brand-steel); }
  .card--tamberline .brand__mark { background: var(--brand-steel); border-radius: 0; }
  .card--orrick .brand__name { color: var(--brand-deep); font-size: 24px; }
  .card--orrick .brand__tagline { color: var(--brand-deep); }
  .card--orrick .brand__mark { background: var(--brand-deep); }

  .contact {
    position: absolute; left: 332px; top: 9px; width: 193px; height: 277px;
    display: flex; flex-direction: column; gap: 6px;
  }
  .contact__band {
    flex: 1;
    border-radius: 44px 0 0 44px;
    box-shadow: -3px 0 0 var(--sheet);
    display: flex; align-items: center; gap: 14px;
    padding-left: 16px;
    color: var(--ink-light);
  }
  .contact__band--person  { background: var(--band-top); }
  .contact__band--web     { background: var(--band-mid); }
  .contact__band--address { background: var(--band-low); }
  .contact__icon { width: 24px; height: 24px; flex: none; fill: var(--ink-light); }
  .contact__text { line-height: 1.15; }
  .contact__name { font-size: 19px; font-weight: 600; }
  .contact__title { font-size: 12px; font-weight: 600; }
  .contact__phone { font-size: 13px; font-weight: 600; }
  .contact__web { font-size: 10px; font-weight: 600; letter-spacing: .6px; line-height: 2; }
  .contact__address { font-size: 13px; font-weight: 600; }
</style>
</head>
<body>

<svg width="0" height="0" style="position:absolute" aria-hidden="true">
  <symbol id="icon-person" viewBox="0 0 24 24">
    <path d="M12 2a5 5 0 0 1 5 5v1.5a5 5 0 0 1-10 0V7a5 5 0 0 1 5-5zM3 22c0-4 3-6.5 6-7.2l3 2.2 3-2.2c3 .7 6 3.2 6 7.2z"/>
  </symbol>
  <symbol id="icon-globe" viewBox="0 0 24 24">
    <g fill="none" stroke="#fff" stroke-width="1.4">
      <circle cx="12" cy="12" r="10"/>
      <ellipse cx="12" cy="12" rx="4.5" ry="10"/>
      <path d="M2 12h20M3.5 7h17M3.5 17h17M12 2v20"/>
    </g>
  </symbol>
  <symbol id="icon-pin" viewBox="0 0 24 24">
    <path fill-rule="evenodd" d="M12 1a8 8 0 0 1 8 8c0 5-8 14-8 14S4 14 4 9a8 8 0 0 1 8-8zm0 4.5a3.5 3.5 0 1 0 0 7 3.5 3.5 0 0 0 0-7z"/>
  </symbol>
</svg>

<!-- Parent company card -->
<section class="card card--voltren">
  <div class="card__backdrop" role="img" aria-label="Faded grayscale photo of an electrical substation with insulators and steel structures"></div>
  <div class="brand">
    <div class="brand__mark"></div>
    <div class="brand__name">Voltren</div>
    <div class="brand__tagline">Assemblies, Inc.</div>
  </div>
  <div class="contact">
    <div class="contact__band contact__band--person">
      <svg class="contact__icon"><use href="#icon-person"/></svg>
      <div class="contact__text"><div class="contact__name">YOUR NAME</div><div class="contact__title">YOUR TITLE HERE</div><div class="contact__phone">+00 00 000 0000</div></div>
    </div>
    <div class="contact__band contact__band--web">
      <svg class="contact__icon"><use href="#icon-globe"/></svg>
      <div class="contact__text contact__web">WWW.WEBSITE.COM<br>EMAILS@WEBSITE.COM</div>
    </div>
    <div class="contact__band contact__band--address">
      <svg class="contact__icon"><use href="#icon-pin"/></svg>
      <div class="contact__text contact__address">1 BUSINESS STREET<br>COMPANY BLVD.<br>0000</div>
    </div>
  </div>
</section>

<!-- Ceramic entity card -->
<section class="card card--brackway">
  <div class="card__backdrop" role="img" aria-label="Faded grayscale photo of an electrical substation with insulators and steel structures"></div>
  <div class="brand">
    <div class="brand__mark"></div>
    <div class="brand__name">Brackway Ceramic, LLC.</div>
    <div class="brand__tagline">A Voltren Assemblies, Inc. Company</div>
  </div>
  <div class="contact">
    <div class="contact__band contact__band--person">
      <svg class="contact__icon"><use href="#icon-person"/></svg>
      <div class="contact__text"><div class="contact__name">YOUR NAME</div><div class="contact__title">YOUR TITLE HERE</div><div class="contact__phone">+00 00 000 0000</div></div>
    </div>
    <div class="contact__band contact__band--web">
      <svg class="contact__icon"><use href="#icon-globe"/></svg>
      <div class="contact__text contact__web">WWW.WEBSITE.COM<br>EMAILS@WEBSITE.COM</div>
    </div>
    <div class="contact__band contact__band--address">
      <svg class="contact__icon"><use href="#icon-pin"/></svg>
      <div class="contact__text contact__address">1 BUSINESS STREET<br>COMPANY BLVD.<br>0000</div>
    </div>
  </div>
</section>

<!-- Breaker entity card -->
<section class="card card--tamberline">
  <div class="card__backdrop" role="img" aria-label="Faded grayscale photo of an electrical substation with insulators and steel structures"></div>
  <div class="brand">
    <div class="brand__mark"></div>
    <div class="brand__name">Tamberline Breaker</div>
    <div class="brand__tagline">A Voltren Assemblies Inc. Company</div>
  </div>
  <div class="contact">
    <div class="contact__band contact__band--person">
      <svg class="contact__icon"><use href="#icon-person"/></svg>
      <div class="contact__text"><div class="contact__name">YOUR NAME</div><div class="contact__title">YOUR TITLE HERE</div><div class="contact__phone">+00 00 000 0000</div></div>
    </div>
    <div class="contact__band contact__band--web">
      <svg class="contact__icon"><use href="#icon-globe"/></svg>
      <div class="contact__text contact__web">WWW.WEBSITE.COM<br>EMAILS@WEBSITE.COM</div>
    </div>
    <div class="contact__band contact__band--address">
      <svg class="contact__icon"><use href="#icon-pin"/></svg>
      <div class="contact__text contact__address">1 BUSINESS STREET<br>COMPANY BLVD.<br>0000</div>
    </div>
  </div>
</section>

<!-- Metering entity card -->
<section class="card card--orrick">
  <div class="card__backdrop" role="img" aria-label="Faded grayscale photo of an electrical substation with insulators and steel structures"></div>
  <div class="brand">
    <div class="brand__mark"></div>
    <div class="brand__name">Orrick Metering<br>Devices Corporation</div>
    <div class="brand__tagline">A Voltren Assemblies, Inc. Company</div>
  </div>
  <div class="contact">
    <div class="contact__band contact__band--person">
      <svg class="contact__icon"><use href="#icon-person"/></svg>
      <div class="contact__text"><div class="contact__name">YOUR NAME</div><div class="contact__title">YOUR TITLE HERE</div><div class="contact__phone">+00 00 000 0000</div></div>
    </div>
    <div class="contact__band contact__band--web">
      <svg class="contact__icon"><use href="#icon-globe"/></svg>
      <div class="contact__text contact__web">WWW.WEBSITE.COM<br>EMAILS@WEBSITE.COM</div>
    </div>
    <div class="contact__band contact__band--address">
      <svg class="contact__icon"><use href="#icon-pin"/></svg>
      <div class="contact__text contact__address">1 BUSINESS STREET<br>COMPANY BLVD.<br>0000</div>
    </div>
  </div>
</section>

</body>
</html>
```